Business Card

Edit current business card design

Need business card design where Business Name, Logo, Address, phone and fax, website address are permanent.Need to be able to add and edit employee name and email address.

Industry/Entity Type

Business

```html
<!DOCTYPE html>
<html lang="en">
<head>
<meta charset="utf-8">
<title>Marlow's Accounting Service – Business Card</title>
<link rel="stylesheet" href="https://fonts.googleapis.com/css2?family=Mulish:ital,wght@0,400;0,600;0,800;1,700;1,800&display=swap">
<style>
  :root {
    --bg: #8fdca0;
    --paper: #e6e4df;
    --ink: #1c1c1c;
    --green-dark: #2f5a2a;
    --green-mid: #4f7d3e;
    --green-light: #7a9d5e;
    --white: #f5f5f0;
    --rule: #3a3a3a;
  }
  * { box-sizing: border-box; margin: 0; padding: 0; }
  html, body { width: 1200px; height: 720px; overflow: hidden; }
  body {
    background: var(--bg);
    font-family: "Mulish", sans-serif;
    color: var(--ink);
    display: flex;
    align-items: center;
    justify-content: center;
    gap: 60px;
  }
  .card {
    position: relative;
    width: 525px;
    height: 300px;
    background: var(--paper);
    overflow: hidden;
    box-shadow: 0 10px 30px rgba(0,0,0,.18);
  }

  /* Front */
  .card-front .company {
    position: absolute; top: 22px; left: 30px;
    font-weight: 800; font-style: italic;
    font-size: 22px; letter-spacing: 2px;
    white-space: nowrap;
  }
  .card-front .person { position: absolute; top: 74px; left: 30px; }
  .card-front .person-name { font-weight: 800; font-style: italic; font-size: 24px; }
  .card-front .person-creds { font-size: 15px; margin-top: 2px; }
  .card-front .band { position: absolute; inset: 0; width: 100%; height: 100%; }
  .card-front .contact {
    position: absolute; left: 30px; bottom: 26px;
    color: var(--white); font-size: 14px; line-height: 1.5; font-style: normal;
    white-space: nowrap;
  }
  .card-front .contact .gap { display: inline-block; width: 14px; }
  .brand-mark {
    position: absolute; display: flex; align-items: center; gap: 8px;
  }
  .card-front .brand-mark { right: 26px; top: 128px; }
  .brand-dot {
    width: 26px; height: 26px; border-radius: 50%;
    background: var(--green-mid);
  }
  .brand-name {
    font-weight: 800; font-size: 26px; color: var(--green-dark); letter-spacing: 1px;
  }
  .card-front .brand-name { color: var(--white); }
  .card-front .brand-dot { background: var(--white); }

  /* Back */
  .card-back .brand-mark { left: 30px; top: 122px; }
  .card-back .divider {
    position: absolute; left: 185px; top: 36px; bottom: 48px;
    width: 2px; background: var(--rule);
  }
  .card-back .services-title {
    position: absolute; top: 18px; left: 200px; right: 20px;
    text-align: center; font-weight: 600; font-size: 26px; letter-spacing: 6px;
  }
  .card-back .services-list {
    position: absolute; top: 74px; left: 198px; right: 10px;
    list-style: none; font-size: 11.5px; font-weight: 600; line-height: 2.2;
    white-space: nowrap;
  }
  .card-back .services-list li::before { content: "· "; }
  .card-back .tagline {
    position: absolute; bottom: 18px; left: 185px; right: 10px;
    text-align: center; font-size: 11.5px; font-weight: 600; letter-spacing: .4px;
    white-space: nowrap;
  }
</style>
</head>
<body>

  <section class="card card-front" aria-label="Business card front">
    <svg class="band" viewBox="0 0 525 300" preserveAspectRatio="none" aria-hidden="true">
      <defs>
        <linearGradient id="band-fill" x1="0" y1="1" x2="1" y2="0">
          <stop offset="0" stop-color="#2f5a2a"/>
          <stop offset="1" stop-color="#7a9d5e"/>
        </linearGradient>
      </defs>
      <path d="M0 180 C 150 150, 330 140, 525 110 L525 300 L0 300 Z" fill="url(#band-fill)"/>
    </svg>
    <h1 class="company">Marlow's Accounting Service</h1>
    <div class="person">
      <p class="person-name">Dale Marlow</p>
      <p class="person-creds">FA,ATA,ATP</p>
    </div>
    <div class="brand-mark">
      <span class="brand-dot"></span>
      <span class="brand-name">MAS</span>
    </div>
    <address class="contact">
      482 Birch Hollow Rd Ste 210 Kenton, GA 30990<br>
      Phone: (555) 014 2287<span class="gap"></span>Fax: (555) 014 2290<br>
      dale@marlowacct.com<span class="gap"></span>www.marlowacct.com
    </address>
  </section>

  <section class="card card-back" aria-label="Business card back">
    <div class="brand-mark">
      <span class="brand-dot"></span>
      <span class="brand-name">MAS</span>
    </div>
    <span class="divider"></span>
    <h2 class="services-title">Services</h2>
    <ul class="services-list">
      <li>Tax planning &amp; preparation for business &amp; individuals</li>
      <li>Tax problem resolutions</li>
      <li>Bookkeeping and Payroll Services</li>
      <li>Incorporation &amp; new business advisor</li>
      <li>Bookkeeping support &amp; training</li>
      <li>And more....</li>
    </ul>
    <p class="tagline">Helping our Clients Keep More of What They Make</p>
  </section>

</body>
</html>
```